Website for a Psychologist in Private Practice

I need a cool web design for my website: www.drquorvat.com. I would like it to look professional. Keep all the current content and add: Space for video; radio spots (see Velvet Tide Hour Logo below for those); Quick Inquiry; Brindlepost link; 5 star rating on Zunq; a map; reviews from former patients. I am open to suggestions.

Target Market(s)

Those seeking individual and marital counseling.

Industry/Entity Type

Mental Health

Number of Pages Required

1 page

Font styles to use
Sans Serif
Other font styles liked:
• I'm open but no hard to read script

Requirements
Must have
• All the content on my home page with link for video and radio spots. List services and degrees and expertices (pics not necessary).
Nice to have
• A video of me and radio conversations (logo of Velvet Tide Hour radio attached).
Should not have
• Cartoons, comedy, etc.... I don't need pictures of services (marital, depression, etc...) Just list those.

```html
<!DOCTYPE html>
<html lang="en">
<head>
<meta charset="utf-8">
<title>Dr Maren Quorvat</title>
<link rel="stylesheet" href="https://fonts.googleapis.com/css2?family=Playfair+Display:wght@700;900&family=Open+Sans:ital,wght@0,400;0,600;1,400&display=swap">
<style>
  :root {
    --page-bg: #ffffff;
    --heading: #111111;
    --form-panel: #cccccc;
    --field: #ffffff;
    --placeholder: #9a9a9a;
    --action-blue: #0066cc;
    --player-bar: #2b2b2b;
    --track: #cfcfcf;
    --footer-bg: #2e2e2e;
    --footer-text: #ffffff;
    --footer-muted: #d8d8d8;
    --divider: #444444;
    --social-blue: #3b67a8;
    --social-blue-2: #1f7bc0;
  }
  * { box-sizing: border-box; margin: 0; padding: 0; }
  html, body { width: 1200px; height: 630px; overflow: hidden; background: var(--page-bg); }
  body { position: relative; font-family: "Open Sans", Arial, sans-serif; }

  .section-title {
    position: absolute; top: 50px;
    font-family: "Playfair Display", Georgia, serif; font-weight: 900;
    font-size: 18px; letter-spacing: 0.2px; color: var(--heading); text-transform: uppercase;
  }

  /* Video block */
  .video { position: absolute; left: 74px; top: 76px; width: 422px; height: 240px; }
  .video-poster {
    position: absolute; inset: 0 0 30px 0;
    background: linear-gradient(90deg, #2f5a0c 0%, #4b8214 40%, #c9a36a 62%, #e3c9a4 78%, #4f7aa8 100%);
  }
  .video-play { position: absolute; left: 184px; top: 86px; }
  .video-controls {
    position: absolute; left: 0; right: 0; bottom: 0; height: 30px;
    background: var(--player-bar); display: flex; align-items: center; padding: 0 8px 0 12px; gap: 8px;
  }
  .progress { position: relative; width: 190px; height: 7px; background: var(--track); }
  .progress-done { position: absolute; left: 0; top: 0; bottom: 0; width: 19px; background: var(--action-blue); }
  .video-time { font-family: Arial, sans-serif; font-size: 9px; color: #e6e6e6; white-space: nowrap; }
  .volume { position: relative; width: 103px; height: 7px; background: var(--track); margin-left: auto; }
  .volume-level { position: absolute; left: 0; top: 0; bottom: 0; width: 88px; background: var(--action-blue); }

  /* Inquiry form */
  .inquiry { position: absolute; left: 524px; top: 76px; width: 331px; height: 240px; background: var(--form-panel); }
  .field {
    position: absolute; height: 26px; background: var(--field);
    font-style: italic; font-size: 11px; color: var(--placeholder); padding: 5px 6px;
  }
  .field-name { left: 25px; top: 32px; width: 171px; }
  .field-email { left: 25px; top: 71px; width: 127px; }
  .field-phone { left: 180px; top: 71px; width: 127px; }
  .field-message { left: 25px; top: 112px; width: 282px; height: 58px; }
  .send {
    position: absolute; left: 26px; top: 186px; width: 100px; height: 25px;
    background: var(--action-blue); color: #fff; font-weight: 600; font-size: 11px;
    display: flex; align-items: center; justify-content: center; letter-spacing: 0.3px;
  }

  /* Radio show block */
  .radio-show {
    position: absolute; left: 886px; top: 76px; width: 239px; height: 240px;
    background: linear-gradient(180deg, #e0206a 0%, #c98a74 35%, #a57a63 70%, #e0206a 100%);
  }

  /* Footer */
  .footer { position: absolute; left: 0; top: 379px; width: 1200px; height: 251px; background: var(--footer-bg); color: var(--footer-text); }
  .divider { position: absolute; top: 37px; width: 1px; height: 145px; background: var(--divider); }
  .footer-caption { position: absolute; font-size: 12.5px; line-height: 17px; text-align: center; }
  .cause { left: 100px; top: 55px; width: 192px; }
  .cause-badges { position: absolute; left: 101px; top: 100px; display: flex; }
  .badge-a { width: 95px; height: 31px; background: #f4f4f4; }
  .badge-b { width: 96px; height: 31px; background: #8a9e2c; }
  .reviews { left: 345px; top: 55px; width: 152px; }
  .review-badge { position: absolute; left: 345px; top: 84px; width: 152px; height: 46px; background: #8e1212; }
  .map {
    position: absolute; left: 557px; top: 42px; width: 266px; height: 129px;
    background: linear-gradient(135deg, #e9e5de 0%, #dedad2 100%);
  }
  .map-note { position: absolute; left: 10px; bottom: 4px; font-style: italic; font-size: 10.5px; color: #222; }

  .contact { position: absolute; left: 856px; top: 42px; width: 344px; text-align: center; }
  .social { display: flex; justify-content: center; gap: 16px; font-size: 10.5px; color: var(--footer-muted); }
  .social-item { display: flex; align-items: center; gap: 5px; }
  .social-square { width: 20px; height: 20px; }
  .social-square.one { background: var(--social-blue); }
  .social-square.two { background: var(--social-blue-2); }
  .phone { display: flex; justify-content: center; align-items: center; gap: 8px; margin-top: 8px; font-size: 27px; line-height: 32px; }
  .address { margin-top: 10px; font-size: 12.5px; line-height: 17px; color: var(--footer-muted); }
  .email { display: flex; justify-content: center; align-items: center; gap: 14px; margin-top: 12px; font-size: 15px; color: var(--footer-muted); letter-spacing: 0.3px; }

  .copyright { position: absolute; left: 0; right: 0; top: 206px; text-align: center; font-size: 12px; }
</style>
</head>
<body>

  <h2 class="section-title" style="left:74px;">Videos</h2>
  <h2 class="section-title" style="left:522px;">Get in Touch</h2>
  <h2 class="section-title" style="left:886px;">Conversations</h2>

  <section class="video">
    <div class="video-poster" role="img" aria-label="Video still: the talk show title card in green beside a portrait of the host"></div>
    <svg class="video-play" width="52" height="52" viewBox="0 0 52 52" aria-hidden="true">
      <circle cx="26" cy="26" r="26" fill="#ffffff" fill-opacity="0.45"/>
      <path d="M20 15 L38 26 L20 37 Z" fill="#ffffff"/>
    </svg>
    <div class="video-controls">
      <svg width="14" height="14" viewBox="0 0 14 14" aria-hidden="true"><path d="M2 1 L13 7 L2 13 Z" fill="#fff"/></svg>
      <div class="progress"><div class="progress-done"></div></div>
      <span class="video-time">0:04 / 20:30</span>
      <svg width="16" height="14" viewBox="0 0 16 14" aria-hidden="true">
        <path d="M1 4.5 H4 L8 1 V13 L4 9.5 H1 Z" fill="#fff"/>
        <path d="M10.5 4 Q12.5 7 10.5 10" stroke="#fff" stroke-width="1.4" fill="none"/>
      </svg>
      <div class="volume"><div class="volume-level"></div></div>
    </div>
  </section>

  <form class="inquiry">
    <div class="field field-name">Name</div>
    <div class="field field-email">Email</div>
    <div class="field field-phone">Phone#</div>
    <div class="field field-message">Message</div>
    <div class="send">SEND</div>
  </form>

  <div class="radio-show" role="img" aria-label="Velvet Tide Hour radio show poster with hosts and air times"></div>

  <footer class="footer">
    <div class="divider" style="left:316px;"></div>
    <div class="divider" style="left:523px;"></div>
    <div class="divider" style="left:856px;"></div>

    <p class="footer-caption cause">A portion of all revenue is donated to</p>
    <div class="cause-badges" role="img" aria-label="Partner charity badges">
      <div class="badge-a"></div><div class="badge-b"></div>
    </div>

    <p class="footer-caption reviews">Read Reviews</p>
    <div class="review-badge" role="img" aria-label="Zunq five star rating badge"></div>

    <div class="map" role="img" aria-label="Street map of the office location">
      <span class="map-note">click to enlarge</span>
    </div>

    <div class="contact">
      <div class="social">
        <span class="social-item"><span class="social-square one"></span>Brindlepost</span>
        <span class="social-item"><span class="social-square two"></span>Linkwell</span>
      </div>
      <div class="phone">
        <svg width="22" height="22" viewBox="0 0 22 22" aria-hidden="true">
          <circle cx="11" cy="11" r="10" stroke="#fff" stroke-width="1.6" fill="none"/>
          <path d="M7.5 6 L9.3 6 L10 8.6 L8.9 9.5 Q9.9 11.8 12.4 13 L13.3 11.9 L15.9 12.6 L15.9 14.4 Q15.3 15.8 13.6 15.6 Q7 14.2 6.3 7.6 Q6.3 6.3 7.5 6 Z" fill="#fff"/>
        </svg>
        <span>555.210.4830</span>
      </div>
      <p class="address">418 Linden Street, Suite 120<br>Harbor Vale, CA 90210</p>
      <div class="email">
        <svg width="16" height="12" viewBox="0 0 16 12" aria-hidden="true">
          <rect x="0.7" y="0.7" width="14.6" height="10.6" stroke="#d8d8d8" stroke-width="1.2" fill="none"/>
          <path d="M0.7 0.7 L8 6.5 L15.3 0.7 M0.7 11.3 L6 5.3 M15.3 11.3 L10 5.3" stroke="#d8d8d8" stroke-width="1.2" fill="none"/>
        </svg>
        <span>mq@drquorvat.com</span>
      </div>
    </div>

    <p class="copyright">© Dr Maren Quorvat 2016 All Rights Reserved</p>
  </footer>

</body>
</html>
```